K & R Ground Works. Business card design

We need a business card designed for a new business. We have a bulldozer and tractor service. We clear land and make wildlife food plots. We provide disking, bush hogging, and site prep services.
I have attached an image of a business card that I like and would like my business cards to look similar.

Target Market(s)

anyone needing bulldozer and/or tractor services

Industry/Entity Type

Business

Contact Information for Business Card

K & R Ground Works, Operated by 7-T-Ranch
Dale Whitcomb
601-555-0148
dwk4821@mailbarn.example

Font styles to use
Sans Serif

Colors

Designer to choose colors to be used in the design.

Requirements
Must have
• image of tractor and bulldozer
• Land Clearing
• Wildlife food plots
• Bush Hogging
• Disking
• Site prep
Nice to have
• i have included a image of a business card that i like. I would like mine to be similar.

```html
<!DOCTYPE html>
<html lang="en">
<head>
<meta charset="utf-8">
<title>K &amp; R Ground Works – Business Card</title>
<link rel="stylesheet" href="https://fonts.googleapis.com/css2?family=Roboto+Condensed:wght@400;700&family=Roboto:wght@400;500&display=swap">
<style>
  :root {
    --page-bg: #262626;
    --olive: #9c9e3c;
    --olive-dark: #84862e;
    --olive-text: #a7aa3c;
    --brown: #6a4313;
    --brown-text: #5a3510;
    --silver-light: #f2f2f2;
    --silver-dark: #9a9a9a;
    --white: #ffffff;
    --tagline: #f4f1d8;
  }
  html, body {
    margin: 0;
    width: 1200px;
    height: 771px;
    overflow: hidden;
    background: var(--page-bg);
  }
  .card {
    position: absolute;
    left: 60px;
    top: 76px;
    width: 1080px;
    height: 619px;
    display: block;
  }
  .brand-name { font-family: "Roboto Condensed", sans-serif; font-weight: 700; font-size: 21px; fill: var(--brown-text); letter-spacing: 0.3px; }
  .brand-tagline { font-family: "Roboto Condensed", sans-serif; font-weight: 700; font-size: 10px; fill: var(--tagline); }
  .contact-name { font-family: "Roboto Condensed", sans-serif; font-weight: 700; font-size: 20px; fill: var(--white); }
  .contact-role { font-family: "Roboto", sans-serif; font-size: 14px; fill: var(--white); }
  .contact-line { font-family: "Roboto", sans-serif; font-size: 13px; fill: var(--white); }
  .website { font-family: "Roboto Condensed", sans-serif; font-weight: 700; font-size: 18px; fill: var(--white); }
  .services-title { font-family: "Roboto Condensed", sans-serif; font-weight: 700; font-size: 16px; fill: var(--olive-text); }
  .service-item { font-family: "Roboto", sans-serif; font-size: 14px; fill: var(--white); }
  .service-dot { fill: var(--olive-text); }
</style>
</head>
<body>
<svg class="card" viewBox="300 213 600 344" xmlns="http://www.w3.org/2000/svg">
  <defs>
    <clipPath id="card-shape"><rect x="300" y="213" width="600" height="344" rx="14"/></clipPath>
    <linearGradient id="olive-fill" x1="0" y1="0" x2="1" y2="1">
      <stop offset="0" stop-color="#a2a440"/><stop offset="1" stop-color="#8e9034"/>
    </linearGradient>
    <linearGradient id="tractor-fill" x1="0" y1="0" x2="0" y2="1">
      <stop offset="0" stop-color="#4f6a33"/><stop offset="0.55" stop-color="#b5552a"/><stop offset="1" stop-color="#8c8a5e"/>
    </linearGradient>
    <linearGradient id="dozer-fill" x1="0" y1="0" x2="1" y2="1">
      <stop offset="0" stop-color="#6f6448"/><stop offset="0.6" stop-color="#9a8a4a"/><stop offset="1" stop-color="#7d7560"/>
    </linearGradient>
    <linearGradient id="silver" x1="0" y1="0" x2="1" y2="1">
      <stop offset="0" stop-color="var(--silver-light)"/><stop offset="1" stop-color="var(--silver-dark)"/>
    </linearGradient>
  </defs>

  <g clip-path="url(#card-shape)">
    <rect class="panel-contact" x="300" y="213" width="392" height="202" fill="url(#olive-fill)" role="img" aria-label="Faded photo of a bulldozer behind the contact details"/>
    <rect class="photo-tractor" x="693" y="213" width="207" height="156" fill="url(#tractor-fill)" role="img" aria-label="Photo of an orange tractor with front loader in a field"/>
    <rect class="photo-dozer" x="300" y="417" width="334" height="140" fill="url(#dozer-fill)" role="img" aria-label="Photo of a bulldozer clearing land and soil"/>
    <rect class="panel-services" x="636" y="370" width="264" height="187" fill="var(--brown)"/>

    <rect class="divider" x="300" y="412" width="340" height="7" fill="url(#silver)"/>
    <rect class="divider" x="631" y="412" width="6" height="145" fill="url(#silver)"/>
    <rect class="divider" x="689" y="213" width="6" height="170" fill="url(#silver)"/>
    <rect class="divider" x="689" y="366" width="211" height="7" fill="url(#silver)"/>

    <circle class="emblem-ring" cx="664" cy="392" r="37" fill="url(#silver)"/>
    <circle class="emblem" cx="664" cy="392" r="29" fill="var(--white)"/>
  </g>

  <text class="brand-name" x="340" y="272">K &amp; R GROUND WORKS</text>
  <text class="brand-tagline" x="340" y="287">FOR ALL OF YOUR LAND IMPROVEMENT NEEDS</text>

  <text class="contact-name" x="340" y="328">DALE WHITCOMB</text>
  <text class="contact-role" x="340" y="346">OWNER</text>

  <path class="icon-phone" fill="var(--white)" d="M343 357.5c.6-.6 1.4-.6 1.9 0l1.3 1.6c.4.5.3 1.2-.2 1.6l-.7.6c.6 1.3 1.6 2.3 2.9 2.9l.6-.7c.4-.5 1.1-.6 1.6-.2l1.6 1.3c.6.5.6 1.3 0 1.9l-.8.8c-.9.9-2.6.8-4.6-.5-1.6-1-3-2.4-4-4-1.3-2-1.4-3.7-.5-4.6z"/>
  <text class="contact-line" x="359" y="368">601-555-0148</text>
  <rect class="icon-mail" x="341" y="377" width="11" height="8" fill="var(--white)"/>
  <path d="M341 377l5.5 4.5 5.5-4.5" fill="none" stroke="var(--olive-dark)" stroke-width="1"/>
  <text class="contact-line" x="359" y="386">dwk4821@mailbarn.example</text>

  <text class="website" x="341" y="524">WWW.KRGROUNDWORKS.EXAMPLE</text>

  <text class="services-title" x="720" y="449">WE CREADED</text>
  <circle class="service-dot" cx="723" cy="462" r="2.2"/>
  <text class="service-item" x="732" y="467">Land Clearing</text>
  <circle class="service-dot" cx="723" cy="480" r="2.2"/>
  <text class="service-item" x="732" y="485">Wildlife food plots</text>
  <circle class="service-dot" cx="723" cy="498" r="2.2"/>
  <text class="service-item" x="732" y="503">Bush Hogging</text>
  <circle class="service-dot" cx="723" cy="516" r="2.2"/>
  <text class="service-item" x="732" y="521">Disking</text>
  <circle class="service-dot" cx="788" cy="516" r="2.2"/>
  <text class="service-item" x="794" y="521">Site prep</text>
</svg>
</body>
</html>
```